Email Banner: Pale Harbor

Need an email banner for https://pale-harbor.example/ much the same design for the attatched just using the logo and brand as the guidance.

Tagline should be "Essential Whitepapers for Business Professionals" or "Whitepapers featured from the most reputable companies in the industry"

It will be going on an email that looks like this:

https://mailvista.example/emails/preview/fullscreen/a17d3b2e-8c4f-4e1a-9b6d-f24e8a1c5d90

So dont make it to thick and clunky.

Target Market(s)

IT Proffesioanls

Industry/Entity Type

Information Technology

Logo Text

Essential Whitepapers for Business Professionals

Logo styles of interest
Abstract Logo
Font styles to use
Sans Serif

Colors
0054AA
0677BA
7BADD7
CADEEF
E8F1F8

Requirements
Must have
• Logo and colour scheme from the weblink provided: https://pale-harbor.example/

```html
<!DOCTYPE html>
<html lang="en">
<head>
<meta charset="utf-8">
<title>Pale Harbor – Email Banner</title>
<link rel="stylesheet" href="https://fonts.googleapis.com/css2?family=Montserrat:wght@300;400;700&display=swap">
<style>
  :root {
    --harbor-mist: #e8f1f8;
    --harbor-fog: #cadeef;
    --harbor-sky: #7badd7;
    --harbor-sea: #0677ba;
    --harbor-deep: #0054aa;
    --panel-white: #ffffff;
    --brand-ink: #0a1f3d;
    --tagline-ink: #ffffff;
  }
  html, body {
    margin: 0;
    padding: 0;
    overflow: hidden;
    background: var(--panel-white);
  }
  .banner {
    position: relative;
    width: 1200px;
    height: 188px;
    overflow: hidden;
    font-family: "Montserrat", Arial, sans-serif;
  }
  .banner__backdrop {
    position: absolute;
    inset: 0;
    display: block;
  }
  .brand__dot {
    position: absolute;
    left: 56px;
    top: 68px;
    width: 72px;
    height: 72px;
    border-radius: 50%;
    background: var(--harbor-sea);
  }
  .brand__name {
    position: absolute;
    left: 161px;
    top: 76px;
    margin: 0;
    font-weight: 700;
    font-size: 54px;
    line-height: 1;
    color: var(--brand-ink);
    white-space: nowrap;
  }
  .tagline {
    position: absolute;
    left: 612px;
    top: 69px;
    margin: 0;
    color: var(--tagline-ink);
    font-size: 29px;
    line-height: 29px;
    font-weight: 300;
    white-space: nowrap;
  }
  .tagline__strong {
    font-weight: 700;
  }
</style>
</head>
<body>
  <div class="banner">
    <svg class="banner__backdrop" width="1200" height="188" viewBox="0 0 1200 188" aria-hidden="true">
      <defs>
        <linearGradient id="bandGradient" x1="0" y1="0" x2="1" y2="0">
          <stop offset="0" stop-color="var(--harbor-fog)"/>
          <stop offset="0.25" stop-color="var(--harbor-sky)"/>
          <stop offset="0.5" stop-color="var(--harbor-sea)"/>
          <stop offset="1" stop-color="var(--harbor-deep)"/>
        </linearGradient>
      </defs>
      <rect width="1200" height="188" fill="url(#bandGradient)"/>
      <path d="M0 21.5 H476 C505 21.5 530 40 537 66 L571 188 H0 Z" fill="var(--panel-white)"/>
    </svg>

    <span class="brand__dot"></span>
    <p class="brand__name">Pale Harbor</p>

    <p class="tagline">Essential Whitepapers<br>for <span class="tagline__strong">Business Professionals</span></p>
  </div>
</body>
</html>
```